I need a letterhead for a newsletter that will go out quarterly to the dentists of the 18th district. It is called "The Cobalt Bulletin" We are in Amarillo TX and have this landmark in the photo as our most prominent feature. If it could be used, that would be cool.
This is a professional organization newsletter so the letterhead should be somewhat professional.

Target Market(s)

Dentists

Industry/Entity Type

Dental

Font styles to use
Serif

Colors

Designer to choose only greyscale colors for use in the design.

Requirements
Must have
• I want the title of "The Cobalt Bulletin" to be the on top with the phrase "Brookmere Valley Dental Guild" written underneath.
Nice to have
• the photo incorporated could be incorporated in black and white or color along the bottom of the letterhead or with the title inside the photo.
Should not have
• I don't want it to be cartoony. I want it to be stylish and elegant and professional.

```html
<!DOCTYPE html>
<html lang="en">
<head>
<meta charset="utf-8">
<title>The Cobalt Bulletin – Letterhead</title>
<link href="https://fonts.googleapis.com/css2?family=Marcellus+SC&family=Lato:wght@400&family=Didact+Gothic&display=swap" rel="stylesheet">
<style>
  :root {
    --backdrop: #e4e4e4;
    --paper: #ffffff;
    --band: #3f3f3f;
    --band-text: #ffffff;
    --photo-light: #9a9a9a;
    --photo-dark: #5c5c5c;
    --photo-border: #ffffff;
    --ink: #3a3a3a;
    --ink-soft: #5a5a5a;
  }
  html, body {
    margin: 0;
    width: 1200px;
    height: 898px;
    overflow: hidden;
    background: var(--backdrop);
  }
  .letterhead {
    position: absolute;
    left: 290px;
    top: 10px;
    width: 620px;
    height: 877px;
    background: var(--paper);
    box-shadow: 0 6px 24px rgba(0, 0, 0, 0.15);
    overflow: hidden;
  }
  .masthead {
    position: absolute;
    left: 0; top: 0;
    width: 100%;
    height: 262px;
    background: var(--band);
  }
  .masthead-photo {
    position: absolute;
    left: 32px;
    top: 20px;
    width: 250px;
    height: 220px;
    border: 3px solid var(--photo-border);
    border-radius: 26px;
    background: linear-gradient(160deg, var(--photo-light) 0%, var(--photo-dark) 100%);
  }
  .masthead-text {
    position: absolute;
    left: 306px;
    top: 66px;
    width: 300px;
    color: var(--band-text);
  }
  .title {
    margin: 0;
    font-family: "Marcellus SC", serif;
    font-weight: 400;
    font-size: 27px;
    line-height: 1.1;
    letter-spacing: 0.3px;
    white-space: nowrap;
  }
  .subtitle {
    margin: 6px 0 14px;
    font-family: "Marcellus SC", serif;
    font-size: 13px;
    letter-spacing: 0.3px;
    white-space: nowrap;
  }
  .contact {
    font-family: "Lato", sans-serif;
    font-size: 10px;
    line-height: 1.7;
  }
  .contact-row { display: flex; gap: 18px; align-items: center; }
  .contact-item { display: inline-flex; align-items: center; gap: 5px; }
  .contact-item svg { width: 10px; height: 10px; }
  .letter-body {
    position: absolute;
    left: 78px;
    top: 360px;
    width: 470px;
    font-family: "Didact Gothic", sans-serif;
    color: var(--ink);
    font-size: 13px;
    line-height: 1.72;
  }
  .letter-body p { margin: 0 0 26px; }
  .letter-body .greeting { margin: 0 0 22px; }
  .letter-body .signature-name {
    margin: 30px 0 2px;
    font-size: 18px;
    color: var(--ink);
  }
  .letter-body .signature-role {
    margin: 0;
    font-size: 11.5px;
    color: var(--ink-soft);
  }
</style>
</head>
<body>
  <main class="letterhead">
    <header class="masthead">
      <div class="masthead-photo" role="img" aria-label="Photograph of the region's best-known rock landmark"></div>
      <div class="masthead-text">
        <h1 class="title">The Cobalt Bulletin</h1>
        <div class="subtitle">Brookmere Valley Dental Guild</div>
        <div class="contact">
          <div>418 Cedarline Ave, Harwick, Dalen County 79105, USA</div>
          <div class="contact-row">
            <span class="contact-item">
              <svg viewBox="0 0 10 10" aria-hidden="true"><path fill="#fff" d="M1 3.2C1 2 2 1.5 5 1.5S9 2 9 3.2V4H7V3.2H3V4H1Z M2.2 4.5H7.8L8.8 8.5H1.2Z"/></svg>
              555.218.0147
            </span>
            <span class="contact-item">
              <svg viewBox="0 0 10 10" aria-hidden="true"><circle cx="5" cy="5" r="4.3" fill="none" stroke="#fff" stroke-width="1"/><path d="M0.8 5H9.2M5 0.8V9.2" stroke="#fff" stroke-width="0.8"/><ellipse cx="5" cy="5" rx="2" ry="4.3" fill="none" stroke="#fff" stroke-width="0.8"/></svg>
              www.brookmereguild.org
            </span>
          </div>
        </div>
      </div>
    </header>

    <section class="letter-body">
      <p class="greeting">Hello Sir/Mam,</p>
      <p>Lorem ipsum dolor sit amet, consectetur adipiscing elit. Donec orci purus, luctus vitae dignissim eu, iaculis sed purus. Vivamus faucibus, ipsum nec aliquet viverra, leo mauris condimentum ligula, sit amet sagittis enim ligula quis arcu. Nam egestas tortor id nisi porttitor mattis. In tortor ante, ultricies in suscipit a, tempus non massa. Vivamus et auctor mi. Fusce vel massa nulla. Phasellus nec eros mauris, et scelerisque orci. Donec malesuada orci vitae nulla accumsan porta a id massa.</p>
      <p>Quisque accumsan iaculis magna sit amet fringilla. Maecenas consequat, magna eget tincidunt semper, odio nibh rutrum mi, id feugiat ante nisi eu risus. Vestibulum nunc orci, rhoncus a placerat in, ultricies in mi. Cras mattis varius eros, vel fringilla nisi suscipit eget. Quisque scelerisque sagittis nulla at porttitor. Mauris a justo et tellus interdum tristique. Sed id augue vitae urna euismod commodo aliquet a quam. Pellentesque arcu velit, cursus et malesuada ut, consequat et diam. Nullam erat sem, rhoncus id ullamcorper vitae, rhoncus et arcu. In ultricies ultricies nulla.</p>
      <p class="signature-name">Owen Hartley</p>
      <p class="signature-role">Co-Founder &amp; CEO</p>
    </section>
  </main>
</body>
</html>
```